2 sided flyer for Insurance Servics

Would like a flyer that talks about who we are, our services, and our process. Attaching relevant information, as well as our Logo and other logos for a few larger insurance carriers that we have access to.

Target Market(s)

Financial Advisors and Insurance Agents

Industry/Entity Type

Finance and Insurance

Colors
0054AA
0677BA
7BADD7
CADEEF
E8F1F8
F0912C
F2A743
F7CA91
FBE8D2
FDF5EE

Requirements
Must have
• Lists, bullet points, pictures, and logos uploaded

```html
<!DOCTYPE html>
<html lang="en">
<head>
<meta charset="utf-8">
<title>Keystone Advisor Group – Two-Sided Flyer</title>
<link rel="stylesheet" href="https://fonts.googleapis.com/css2?family=Montserrat:wght@400;500;600;700&family=Playfair+Display:ital,wght@1,500&display=swap">
<style>
:root{
  --navy:#1f2466;
  --gold:#f9c846;
  --ink:#2b2b33;
  --link:#1f3a9a;
  --grey:#e6e7ec;
  --panel:#eef0f3;
  --rule:#b9bccb;
  --stage:#d6d7db;
  --white:#ffffff;
}
*{box-sizing:border-box;margin:0;padding:0}
html,body{width:918px;height:1200px;overflow:hidden;background:var(--stage)}
body{font-family:'Montserrat',sans-serif;color:var(--ink);position:relative}

.sheet{position:absolute;top:287px;width:708px;height:1000px;background:var(--white);
  transform:scale(.625);transform-origin:0 0;overflow:hidden}
.sheet--front{left:11px}
.sheet--back{left:464.5px}

/* header shared */
.brand{position:absolute;left:22px;top:26px;display:flex;align-items:center;gap:10px}
.brand-mark{width:40px;height:40px;background:var(--navy)}
.brand-name{font-weight:700;font-size:17px;line-height:1.05;color:var(--navy);letter-spacing:.4px}
.contacts{position:absolute;right:30px;top:22px;list-style:none;font-size:13px;line-height:21px}
.contacts li{display:flex;align-items:center;gap:8px}
.contacts li:first-child{font-weight:600}
.contacts svg{width:13px;height:13px;fill:var(--navy)}

/* front */
.hero-photo{position:absolute;left:200px;top:103px;width:508px;height:260px;
  background:linear-gradient(170deg,#f4efd2 0%,#d9d7b4 35%,#8ea24e 68%,#4f6f26 100%)}
.hero-sliver{position:absolute;left:0;top:103px;width:290px;height:22px;background:var(--grey);
  clip-path:polygon(0 0,290px 0,278px 22px,0 22px)}
.about{position:absolute;left:0;top:125px;width:420px;height:198px;background:var(--navy);
  clip-path:polygon(0 0,412px 0,332px 198px,0 198px)}
.about h2{position:absolute;left:22px;top:12px;color:var(--gold);font-size:21px;font-weight:600}
.about p{position:absolute;left:22px;top:42px;width:312px;color:var(--white);font-size:10px;line-height:12.4px;font-weight:500}
.why-tab{position:absolute;left:0;top:326px;width:216px;height:37px;background:var(--gold);
  clip-path:polygon(0 0,216px 0,200px 37px,0 37px)}
.why-tab h2{position:absolute;left:22px;top:5px;font-size:20px;font-weight:600;color:var(--navy)}

.why-intro{position:absolute;left:22px;top:378px;font-size:13px;font-weight:500}
.features{position:absolute;left:22px;top:402px;width:664px;display:grid;grid-template-columns:1fr 1fr;column-gap:36px;row-gap:16px}
.features::after{content:"";position:absolute;left:332px;top:0;width:1px;height:200px;background:var(--rule)}
.feature h3{display:flex;align-items:center;gap:7px;font-size:12.3px;font-weight:600;color:var(--navy);margin-bottom:4px}
.feature h3 svg{width:18px;height:18px;fill:none;stroke:var(--navy);stroke-width:1.6}
.feature p{font-size:10.2px;line-height:12.7px}
.feature em{font-style:normal;color:var(--link)}
.closing{position:absolute;left:22px;top:622px;width:660px;font-size:10.2px;line-height:12.7px}
.cta{position:absolute;left:22px;top:655px;font-size:13.5px;font-weight:600;color:var(--navy)}

.process{position:absolute;left:0;top:709px;width:708px;height:271px;background:var(--navy);border-top:3px solid var(--gold)}
.process-tab{position:absolute;left:0;top:686px;width:192px;height:30px;background:var(--gold);
  clip-path:polygon(0 0,192px 0,180px 30px,0 30px)}
.process-tab h2{position:absolute;left:22px;top:1px;font-size:20px;font-weight:600;color:var(--navy)}
.steps{position:absolute;left:22px;top:22px;width:664px;display:grid;grid-template-columns:1fr 1fr;column-gap:36px;row-gap:10px;color:var(--white)}
.steps::after{content:"";position:absolute;left:332px;top:0;width:1px;height:222px;background:rgba(255,255,255,.6)}
.step h3{display:flex;align-items:center;gap:8px;font-size:12.5px;font-weight:600;color:var(--gold);margin-bottom:7px}
.step-num{width:18px;height:18px;border-radius:50%;background:var(--gold);color:var(--navy);font-size:10.5px;display:flex;align-items:center;justify-content:center}
.step ul{list-style:none}
.step li{position:relative;padding-left:30px;font-size:10.2px;line-height:12.7px;margin-bottom:5px}
.step li svg{position:absolute;left:3px;top:2px;width:9px;height:9px;fill:none;stroke:var(--white);stroke-width:2.4}

.footer-band{position:absolute;left:0;top:980px;width:708px;height:10px;background:var(--grey)}
.footer-tail{position:absolute;left:0;top:990px;width:708px;height:10px;background:var(--navy);
  clip-path:polygon(368px 0,708px 0,708px 10px,360px 10px)}

/* back */
.header-rule{position:absolute;left:0;top:103px;width:708px;height:1px;background:var(--rule)}
.services-title{position:absolute;left:22px;top:112px;font-size:20px;font-weight:600;color:var(--navy)}
.services-intro{position:absolute;left:22px;top:142px;width:300px;font-size:10.2px;line-height:12.6px}
.col-rule{position:absolute;left:330px;width:1px;background:var(--rule)}
.pull-quote{font-family:'Playfair Display',serif;font-style:italic;font-weight:500;color:var(--navy);text-align:center}
.quote-top{position:absolute;left:345px;top:140px;width:345px}
.quote-top .pull-quote{font-size:15px;line-height:18px}
.attribution{font-size:11px;text-align:center;margin-top:8px;color:var(--ink)}
.attribution b{font-weight:700}
.pos{position:absolute;left:22px;top:228px;width:664px;font-size:10.4px;line-height:12.8px}
.pos b{color:var(--navy);font-size:12px;font-weight:600}
.pos-list{position:absolute;left:55px;top:262px;width:640px;list-style:none}
.pos-list li{margin-bottom:12px}
.pos-list h4{font-size:11.5px;font-weight:600;color:var(--navy);position:relative;margin-bottom:6px}
.pos-list h4::before{content:"";position:absolute;left:-12px;top:4px;width:5px;height:5px;border-radius:50%;background:var(--navy)}
.pos-list p{font-size:9.8px;line-height:12.4px}

.concierge{position:absolute;left:0;top:412px;width:708px;height:102px;background:var(--gold)}
.concierge-text{position:absolute;left:22px;top:22px;width:296px;font-size:10.2px;line-height:12.6px}
.concierge-text b{color:var(--navy);font-weight:600;font-size:11.5px}
.concierge .col-rule{top:12px;height:76px;background:var(--navy)}
.quote-mid{position:absolute;left:345px;top:10px;width:345px}
.quote-mid .pull-quote{font-size:15px;line-height:18px}

.panel-navy{position:absolute;left:0;top:517px;width:355px;height:466px;background:var(--navy);color:var(--white);padding:16px 18px 0 22px}
.panel-navy .pull-quote{color:var(--gold);font-size:15px;line-height:18.5px}
.panel-navy .attribution{color:var(--white);margin:6px 0 14px}
.benefit h4{display:flex;align-items:center;gap:7px;font-size:11.5px;font-weight:600;margin-bottom:5px}
.benefit h4 svg{width:10px;height:10px;fill:none;stroke-width:2.4}
.benefit p{font-size:9.8px;line-height:12.4px;margin-bottom:11px}
.panel-navy .benefit h4{color:var(--gold)}
.panel-navy .benefit h4 svg{stroke:var(--gold)}
.panel-navy .pull-quote.closing-quote{margin-top:4px}

.panel-light{position:absolute;left:362px;top:517px;width:346px;height:466px;background:var(--panel);padding:16px 22px 0 16px}
.panel-light .benefit h4{color:var(--navy)}
.panel-light .benefit h4 svg{stroke:var(--navy)}
.panel-light hr{border:0;border-top:1px solid var(--rule);margin:6px 0 12px}
.extra{font-size:9.8px;line-height:12.4px;margin-bottom:10px}
.extra b{color:var(--navy);font-size:11.5px;font-weight:600}

.back-tail{position:absolute;left:0;top:983px;width:708px;height:17px;background:var(--navy);
  clip-path:polygon(362px 0,708px 0,708px 17px,354px 17px)}
</style>
</head>
<body>

<!-- FRONT -->
<main class="sheet sheet--front">
  <header>
    <div class="brand"><span class="brand-mark"></span><span class="brand-name">KEYSTONE<br>ADVISOR GROUP</span></div>
    <ul class="contacts">
      <li><svg viewBox="0 0 24 24"><path d="M6.6 10.8a15 15 0 006.6 6.6l2.2-2.2c.3-.3.7-.4 1-.2 1.1.4 2.3.6 3.6.6.6 0 1 .4 1 1V20c0 .6-.4 1-1 1C10.6 21 3 13.4 3 4c0-.6.4-1 1-1h3.5c.6 0 1 .4 1 1 0 1.3.2 2.5.6 3.6.1.3 0 .7-.2 1z"/></svg>555-201-4470 / 1-800-555-0192</li>
      <li><svg viewBox="0 0 24 24"><path d="M2 5h20v14H2zM3 6l9 7 9-7"/></svg>jordan@keystone-advisor.com</li>
      <li><svg viewBox="0 0 24 24"><path d="M12 2a10 10 0 100 20 10 10 0 000-20zm-1 17.9A8 8 0 014.1 11H8c.1 3.3 1.2 6.3 3 8.9zM8 9H4.1A8 8 0 0111 4.1C9.2 6.7 8.1 9.7 8 9zm2 2h4c-.1 2.8-.9 5.3-2 7.3-1.1-2-1.9-4.5-2-7.3zm0-2c.1-2.8.9-5.3 2-7.3 1.1 2 1.9 4.5 2 7.3zm3 10.9c1.8-2.6 2.9-5.6 3-8.9h3.9a8 8 0 01-6.9 8.9zM16 9c-.1-.7-1.2-2.3-3-4.9A8 8 0 0119.9 9z"/></svg>www.keystoneadvisorgroup.com</li>
    </ul>
  </header>

  <div class="hero-photo" role="img" aria-label="Golfer mid-swing on a sunlit course at sunrise, trees behind"></div>
  <div class="hero-sliver"></div>
  <section class="about">
    <h2>About Us</h2>
    <p>Keystone Advisor Group is a full-service life insurance Brokerage General Agency (BGA) and serves financial advisors, independent insurance agents, and banks throughout the United States. Having served our customers for over 25 years, we are committed to helping financial advisors achieve their goals for their clients. Serving as a one-stop shop for all life insurance solutions, we offer a wide range of insurance products from multiple carriers, giving our advisors and agents access to a variety of options and solutions to meet their clients’ needs.</p>
  </section>
  <div class="why-tab"><h2>Why KAG?</h2></div>

  <p class="why-intro">When you chose to work with KAG, you will add value to your firm...overnight!</p>
  <div class="features">
    <article class="feature">
      <h3><svg viewBox="0 0 24 24"><path d="M12 2l8 3v6c0 5-3.5 9-8 11-4.5-2-8-6-8-11V5z"/><path d="M8 12l3 3 5-6"/></svg>Immediate Risk Management Partner</h3>
      <p>We know insurance and understand your business. Your agents will <em>have access to a wide range of carriers, giving them options</em> to meet client needs. In addition, we only deal in insurance...so rest assured we leave the money management to you!</p>
    </article>
    <article class="feature">
      <h3><svg viewBox="0 0 24 24"><circle cx="12" cy="8" r="4"/><path d="M4 21c0-4.4 3.6-7 8-7s8 2.6 8 7"/></svg>Experienced Insurance Specialists</h3>
      <p>Our Point of Sales Specialists have many years of industry experience, hold various designations, and are licensed to provide a variety of products. These trained professionals <em>are located throughout the country</em> and are ready to provide prompt service to your staff.</p>
    </article>
    <article class="feature">
      <h3><svg viewBox="0 0 24 24"><circle cx="12" cy="7" r="4"/><path d="M6 21v-4a6 6 0 0112 0v4"/></svg>Customized Concierge Service</h3>
      <p>This team of professionals leverage their experience and technology to <em>remove the pain points of writing policies.</em> Comprised of our licensing, application, and case management specialists, we handle every aspect of the process. No more application paperwork or underwriting hassle for your staff!</p>
    </article>
    <article class="feature">
      <h3><svg viewBox="0 0 24 24"><circle cx="12" cy="12" r="9"/><path d="M12 7v5l3 2"/></svg>Save Time and Money</h3>
      <p>We have designed our services to operate efficiently, funded from the compensation we receive by the insurance carriers, meaning <em>no cost to you.</em> Our goal is to increase your production, while eliminating your internal salaries and benefits dedicated to insurance support.</p>
    </article>
  </div>
  <p class="closing">At KAG, we are dedicated to developing lasting relationships with all our of our customers, both current and new. If you have any insurance questions or would like to know how best to work with KAG,</p>
  <p class="cta">Please contact us today contact@keystone-advisor.com</p>

  <section class="process">
    <div class="steps">
      <article class="step">
        <h3><span class="step-num">1</span>Quotes &amp; Analysis</h3>
        <ul>
          <li><svg viewBox="0 0 12 12"><path d="M1 6l3 3 7-7"/></svg>Access to multiple carriers, including most industry leaders.</li>
          <li><svg viewBox="0 0 12 12"><path d="M1 6l3 3 7-7"/></svg>Submit quotes online or simply email our staff.</li>
          <li><svg viewBox="0 0 12 12"><path d="M1 6l3 3 7-7"/></svg>Consult our Specialists to find the best solution for your client.</li>
        </ul>
      </article>
      <article class="step">
        <h3><span class="step-num">2</span>Licensing &amp; Appointment</h3>
        <ul>
          <li><svg viewBox="0 0 12 12"><path d="M1 6l3 3 7-7"/></svg>Confirm agent license and appointment is up to date.</li>
          <li><svg viewBox="0 0 12 12"><path d="M1 6l3 3 7-7"/></svg>If necessary, use our assistance to get appointed in a timely manner.</li>
          <li><svg viewBox="0 0 12 12"><path d="M1 6l3 3 7-7"/></svg>Electronic signatures make the appointment process fast and easy.</li>
        </ul>
      </article>
      <article class="step">
        <h3><span class="step-num">3</span>Applications &amp; Underwriting</h3>
        <ul>
          <li><svg viewBox="0 0 12 12"><path d="M1 6l3 3 7-7"/></svg>Our specialists oversee the entire application and underwriting process.</li>
          <li><svg viewBox="0 0 12 12"><path d="M1 6l3 3 7-7"/></svg>Direct contact with the client, ensuring confidential and private medical history conversation.</li>
          <li><svg viewBox="0 0 12 12"><path d="M1 6l3 3 7-7"/></svg>Utilize technology to provide electronic signatures where possible.</li>
        </ul>
      </article>
      <article class="step">
        <h3><span class="step-num">4</span>Policy Delivery &amp; Payout</h3>
        <ul>
          <li><svg viewBox="0 0 12 12"><path d="M1 6l3 3 7-7"/></svg>Ensure policy documents are delivered in full and on time.</li>
          <li><svg viewBox="0 0 12 12"><path d="M1 6l3 3 7-7"/></svg>Confirm premiums are paid and policies are in force.</li>
          <li><svg viewBox="0 0 12 12"><path d="M1 6l3 3 7-7"/></svg>Facilitate payout for all of your policies.</li>
        </ul>
      </article>
    </div>
  </section>
  <div class="process-tab"><h2>Our Process</h2></div>
  <div class="footer-band"></div>
  <div class="footer-tail"></div>
</main>

<!-- BACK -->
<main class="sheet sheet--back">
  <header>
    <div class="brand"><span class="brand-mark"></span><span class="brand-name">KEYSTONE<br>ADVISOR GROUP</span></div>
    <ul class="contacts">
      <li><svg viewBox="0 0 24 24"><path d="M6.6 10.8a15 15 0 006.6 6.6l2.2-2.2c.3-.3.7-.4 1-.2 1.1.4 2.3.6 3.6.6.6 0 1 .4 1 1V20c0 .6-.4 1-1 1C10.6 21 3 13.4 3 4c0-.6.4-1 1-1h3.5c.6 0 1 .4 1 1 0 1.3.2 2.5.6 3.6.1.3 0 .7-.2 1z"/></svg>555-201-4470 / 1-800-555-0192</li>
      <li><svg viewBox="0 0 24 24"><path d="M2 5h20v14H2zM3 6l9 7 9-7"/></svg>jordan@keystone-advisor.com</li>
      <li><svg viewBox="0 0 24 24"><path d="M12 2a10 10 0 100 20 10 10 0 000-20zm-1 17.9A8 8 0 014.1 11H8c.1 3.3 1.2 6.3 3 8.9zM8 9H4.1A8 8 0 0111 4.1C9.2 6.7 8.1 9.7 8 9zm2 2h4c-.1 2.8-.9 5.3-2 7.3-1.1-2-1.9-4.5-2-7.3zm0-2c.1-2.8.9-5.3 2-7.3 1.1 2 1.9 4.5 2 7.3zm3 10.9c1.8-2.6 2.9-5.6 3-8.9h3.9a8 8 0 01-6.9 8.9zM16 9c-.1-.7-1.2-2.3-3-4.9A8 8 0 0119.9 9z"/></svg>www.keystoneadvisorgroup.com</li>
    </ul>
  </header>
  <div class="header-rule"></div>

  <h2 class="services-title">Our Services</h2>
  <p class="services-intro">As a BGA, our mission is to connect agents and advisors with insurance carriers and help our customers find the correct product that meets each client’s needs. From our experienced Point of Sale Strategists to our professional Concierge Service Team, we provide value every step of the way, at no additional cost!</p>
  <div class="col-rule" style="top:140px;height:72px"></div>
  <div class="quote-top">
    <p class="pull-quote">“ From quote to issue and review to service, each case is an opportunity of quality care. ”</p>
    <p class="attribution"><b>Dana P,</b> New Business Specialist</p>
  </div>

  <p class="pos"><b>Our Point of Sale Strategists</b> work directly with agents and advisors to provide experienced assistance for immediate client needs, as well as maximizing insurance planning to find opportunities for all clients.</p>
  <ul class="pos-list">
    <li><h4>Dedicated Strategists –</h4><p>We develop a personal relationship with each advisor, giving you confidence that we are working in your best interest.<br>Always here to help with quotes and analysis.</p></li>
    <li><h4>Quotes Made Easy –</h4><p>Access our online system or simply email your specialist to receive quotes for your client reviews, life event circumstances, estate needs, or prospect meetings.</p></li>
    <li><h4>National Footprint –</h4><p>Our team is nationwide, allowing us to serve you regardless of location, time zone, or licensing limitations.</p></li>
  </ul>

  <section class="concierge">
    <p class="concierge-text"><b>Our Concierge Service Team</b> is comprised of several specialists. Once an agent moves forward with an application, simply hand it off to our staff, ensuring your policy is processed accurately and delivered in a timely manner.</p>
    <div class="col-rule"></div>
    <div class="quote-mid">
      <p class="pull-quote">“We are the go-to-person for anything the agent needs; we handle everything from A to Z!”</p>
      <p class="attribution"><b>Morgan T,</b> Application Specialist/Case Manager</p>
    </div>
  </section>

  <section class="panel-navy">
    <p class="pull-quote">“Oftentimes clients can be uncomfortable disclosing personal health history to their advisor, but will answer freely with someone in my role. I let clients know we have their best interest at heart.”</p>
    <p class="attribution"><b>Alicia W,</b> Application Specialist</p>
    <div class="benefit"><h4><svg viewBox="0 0 12 12"><path d="M1 6l3 3 7-7"/></svg>Client Confidentiality –</h4><p>Our application specialist contacts the client and takes the application, eliminating the need for clients to share personal medical information with their advisor.</p></div>
    <div class="benefit"><h4><svg viewBox="0 0 12 12"><path d="M1 6l3 3 7-7"/></svg>Proactive Approach –</h4><p>We proactively order medical records and exams for most cases, speeding up the UW process by days if not weeks, resulting in quicker decisions.</p></div>
    <div class="benefit"><h4><svg viewBox="0 0 12 12"><path d="M1 6l3 3 7-7"/></svg>Electronic Signatures –</h4><p>By leveraging technology, we will utilize electronic signature capabilities for both agent and client, speeding up the overall process.</p></div>
    <p class="pull-quote closing-quote">“Our weekly updates keep advisors well informed throughout the process.”</p>
    <p class="attribution"><b>Renee K,</b> Senior Case Manager</p>
  </section>

  <section class="panel-light">
    <div class="benefit"><h4><svg viewBox="0 0 12 12"><path d="M1 6l3 3 7-7"/></svg>Dedicated Case Managers –</h4><p>Your personal case manager gives us a better understanding of your business, expectations, and preferred process.</p></div>
    <div class="benefit"><h4><svg viewBox="0 0 12 12"><path d="M1 6l3 3 7-7"/></svg>No Hassle Paperwork –</h4><p>Our team will handle all application and underwriting needs, assuring a efficient process and less hassle for the agent.</p></div>
    <div class="benefit"><h4><svg viewBox="0 0 12 12"><path d="M1 6l3 3 7-7"/></svg>No Fluff Process –</h4><p>We create a seamless process by gathering what is required for underwriting, eliminating the unnecessary back and forth with clients that often delays the policy and annoys clients.</p></div>
    <div class="benefit"><h4><svg viewBox="0 0 12 12"><path d="M1 6l3 3 7-7"/></svg>Carrier Familiarity –</h4><p>Our experience enables us to provide correct forms from the get-go, as well as properly relay carrier specific processes and manage expectations.</p></div>
    <div class="benefit"><h4><svg viewBox="0 0 12 12"><path d="M1 6l3 3 7-7"/></svg>Agent Licensing –</h4><p>We confirm you are correcty licensed and appointed before applications are initiated. If appointment is needed, we help you get this done in a timely, technology efficient manner.</p></div>
    <hr>
    <p class="extra"><b>Recurring Updates –</b> Your case manager will keep you updated on the status of all cases.</p>
    <p class="extra"><b>Online Case Tracker –</b> This tool allows you to access the status of your cases. All carriers. All cases. All the time.</p>
    <p class="extra"><b>Policy Delivery –</b> we ensure premiums are paid and policy documents are delivered.</p>
  </section>
  <div class="back-tail"></div>
</main>

</body>
</html>
```